Veltarum

Standard Business Card design.
Sample two-sided design uploaded. White front, Black back.
Would like white shield to be on all black background side.
Willing to look at a couple creative designs, but nothing crazy.
Preference for a classic, confident, strong design.

```html
<!DOCTYPE html>
<html lang="en">
<head>
<meta charset="utf-8">
<title>Veltarum Business Card</title>
<link href="https://fonts.googleapis.com/css2?family=Montserrat:wght@400;500;600;700&display=swap" rel="stylesheet">
<style>
  :root {
    --canvas: #e9e9ea;
    --ink: #111111;
    --black: #0b0b0c;
    --white: #ffffff;
    --silver-light: #f1f1f2;
    --silver-mid: #c9c9cb;
    --silver-dark: #8a8a8c;
    --text-grey: #2a2a2a;
  }
  * { margin: 0; padding: 0; box-sizing: border-box; }
  html, body {
    width: 1200px; height: 900px; overflow: hidden;
    background: var(--canvas);
    font-family: "Montserrat", Arial, sans-serif;
  }
  .stage {
    position: relative; width: 1200px; height: 900px;
    display: flex; align-items: center; justify-content: center; gap: 40px;
  }
  .card {
    position: relative; width: 540px; height: 310px;
    border-radius: 16px; overflow: hidden;
    box-shadow: 0 10px 30px rgba(0,0,0,0.18);
  }
  .card-shape { position: absolute; inset: 0; width: 100%; height: 100%; }
  .brand {
    position: absolute; display: flex; align-items: center; gap: 10px;
    font-weight: 700; font-size: 30px; letter-spacing: 5px; white-space: nowrap;
  }
  .brand-square { width: 14px; height: 14px; flex: none; }
  .brand--dark { color: var(--ink); }
  .brand--dark .brand-square { background: var(--ink); }
  .brand--light { color: var(--white); }
  .brand--light .brand-square { background: var(--white); }
  .back .brand--dark { left: 40px; top: 95px; }
  .back .brand--light { right: 28px; top: 168px; font-size: 18px; letter-spacing: 3px; gap: 8px; }
  .back .brand--light .brand-square { width: 10px; height: 10px; }
  .front .brand--dark { right: 30px; top: 36px; font-size: 20px; letter-spacing: 3px; gap: 8px; }
  .front .brand-square { width: 10px; height: 10px; }
  .address {
    position: absolute; right: 30px; top: 142px; text-align: right;
    font-size: 13px; line-height: 1.4; color: var(--text-grey);
  }
  .person { position: absolute; left: 170px; top: 178px; color: var(--ink); }
  .person-name { font-weight: 700; font-size: 20px; line-height: 24px; }
  .person-role { font-size: 12.5px; line-height: 17px; color: var(--text-grey); }
  .contacts { list-style: none; margin-top: 8px; }
  .contacts li {
    display: flex; align-items: center; gap: 10px;
    font-size: 12.5px; line-height: 17px; color: var(--text-grey);
  }
  .contacts svg { width: 12px; height: 12px; fill: var(--ink); flex: none; }
</style>
</head>
<body>
<main class="stage">

  <section class="card back" aria-label="Card back">
    <svg class="card-shape" viewBox="0 0 540 310" preserveAspectRatio="none">
      <defs>
        <linearGradient id="silverBack" x1="0" y1="0" x2="1" y2="1">
          <stop offset="0" stop-color="var(--silver-light)"/>
          <stop offset="0.6" stop-color="#d8d8da"/>
          <stop offset="1" stop-color="var(--silver-mid)"/>
        </linearGradient>
      </defs>
      <rect width="540" height="310" fill="var(--black)"/>
      <path d="M0,0 H475 C395,14 385,120 330,195 C285,258 190,285 0,285 Z" fill="var(--white)"/>
      <path d="M0,0 H462 C385,18 372,118 320,190 C276,250 185,278 0,278 Z" fill="url(#silverBack)"/>
    </svg>
    <div class="brand brand--dark"><span class="brand-square"></span>VELTARUM</div>
    <div class="brand brand--light"><span class="brand-square"></span>VELTARUM</div>
  </section>

  <section class="card front" aria-label="Card front">
    <svg class="card-shape" viewBox="0 0 540 310" preserveAspectRatio="none">
      <defs>
        <linearGradient id="silverFront" x1="1" y1="0" x2="0" y2="1">
          <stop offset="0" stop-color="#b9b9bb"/>
          <stop offset="0.5" stop-color="#dcdcde"/>
          <stop offset="1" stop-color="var(--silver-light)"/>
        </linearGradient>
      </defs>
      <rect width="540" height="310" fill="var(--white)"/>
      <path d="M0,0 H540 V26 C520,116 430,132 320,136 C180,142 112,166 100,310 H0 Z" fill="var(--silver-dark)"/>
      <path d="M0,0 H540 V18 C520,108 430,124 320,128 C175,134 103,158 88,310 H0 Z" fill="var(--white)"/>
      <path d="M0,0 H540 V10 C520,100 430,116 320,120 C170,126 95,150 75,310 H0 Z" fill="url(#silverFront)"/>
    </svg>
    <div class="brand brand--dark"><span class="brand-square"></span>VELTARUM</div>
    <p class="address">418 Harbor Line Ave, #112<br>Millbrook, OH 43190</p>
    <div class="person">
      <h1 class="person-name">Adrian Koval</h1>
      <p class="person-role">Managing Director</p>
      <ul class="contacts">
        <li><svg viewBox="0 0 12 12"><path d="M1,3 Q6,0 11,3 L10,5 L8,4.5 L8,3.5 Q6,3 4,3.5 L4,4.5 L2,5 Z M2.5,6 H9.5 L10,11 H2 Z"/></svg>877-555-0142</li>
        <li><svg viewBox="0 0 12 12"><path d="M3.5,0.5 H8.5 V11.5 H3.5 Z M4.5,1.5 V9.5 H7.5 V1.5 Z" fill-rule="evenodd"/></svg>877-555-0142</li>
        <li><svg viewBox="0 0 12 12"><path d="M0.5,2.5 H11.5 V9.5 H0.5 Z M1.5,3.5 L6,7 L10.5,3.5 Z" fill-rule="evenodd"/></svg>info@veltarumgroup.com</li>
        <li><svg viewBox="0 0 12 12"><circle cx="6" cy="6" r="5.5"/><path d="M1,6 H11 M6,0.5 V11.5" stroke="#fff" stroke-width="0.8"/></svg>www.veltarumgroup.com</li>
      </ul>
    </div>
  </section>

</main>
</body>
</html>
```